Mobile Repair Service on location needs a Web Design

We are starting a new mobile device repair service called Gadget Haven and our website needs a design!

Hello Designers!
First, we'd like to make clear this is more than a simple web design contest, we want the designers to create an idea. We want someone who can create the whole theme of the service's we provide. We want someone that can help design our visual branding, help us communicate a sentiment. And we are willing to pay for that.

Who are we?
Our company is based in Rotterdam, the Netherlands. We provide different services for all kinds of electronic devices. The kind of services we provide are, among other things, installations of hardware and software and the repair of broken or malfunctioning devices.
We are starting a new service that offers mobile device repairs on location, be it at the home of our customers, their office, or any other place. Just give us the address and we will come to you for the repair job. This is also our main USP. We have multiple skilled engineers who drive trough the country on a daily basis and can be on location within a working day. Repair is done immediately onsite while the customer waits. At this stage we will start with the smartphone product-group within the mobile devices. In a second phase we might also add tablets.
People don't want to be without their phone for weeks because of some parts that needed to be ordered by a repair center they had to sent their phone to. We offer a fully functional mobile repair center in the form of specially customized vans. These vans have all the tools and utilities needed by our engineers to safely repair your mobile device. Your phone is being repaired directly in front of you, the next business-day, on a location you desire.

For this new service we are creating a website called Gadget Haven. The website needs a story and matching design and this is where you come in. We are not looking for a simple template design we can get from any place. We need a story. We want you to create an idea, build a unique theme or vision that helps sell the product/service. This goes beyond the design of the website. We need the whole package, the design you are creating needs to have returning elements like icons, color use, images, maybe even characters etc. You name it! There needs to be a common thread in the design so we can reuse elements in, for example, the email templates, the work order or receipt we give to our customers (we may contact the winner of the contest to design these for us as well!).

The name 'Gadget Haven' is chosen. Haven (short for rehabilitate) has a bold and playful tone to it and the design needs to reflect the name. So we're looking for a somewhat playful and cheeky design. Definitely not too serious and definitely modern. We already got a logo that we love and that fit's this description (see attached design documents for the logo). It's bold, powerful and fun. Our web design needs to reflect this as well and has to fit in with our logo.
We would really like it if the design somehow incorporates elements that highlight our unique selling points (repairs on location, we come to you etc.). We would really like some form of story telling in the design. Think clumsy people breaking their phones. Teenagers in tears because they have no access to their friends. People nowadays have the need to always be 'connected'. What happens when your phone is broken or malfunctioning? We're handling tech, we are nerds and a little bit weird, but we're professionals and here to help you with your problem. The sentiment Wire Troop tries to communicate is something we really like. We're looking for fresh idea's, anything goes!

In an overview all Unique Selling Points of the Gadget haven service:
- Professional service on location. Don’t ship to us we will come to you!
- Clear pricing upfront. No hidden cost.
- Next business-day repair.
- Backed by a professional call center open 12 hours a day and open on a Saturday as well
- Backed by a professional repair center with more then 12 years of experience
- Repair is done by certified engineers
- 1 year warranty on the repair

The process:
The main function of our website will be for customers to make a repair request. A customer will visit our website and can make a repair request immediately by going through a 'request-order-flow'. In this flow he or she will need to fill in some forms and can select wich type/model/brand of mobile device he or she has and what parts need to be repaired. After a request is placed we will call the customer back (within an hour) for a short intake and to set a date/time and location. Our engineer will meet the customer at the specified location and will repair the device onsite in one of our mobile repair centers, which is a specialized van equipped with all the tools needed for device restorations.
So in short the steps are:
- Choose your device and repair job
- Place the order
- Get a callback within the hour
- Set date and location
- We will come to you.

Website functionality:
Our website is our main form of communication. So the sentiment we want to communicate needs be reflected in the design. We need a main/front page designed (preferably a long scrolling page design) containing:
1. Customers will be able to request a repair job directly on our website. So there will need to be a prominent button/link at the top of our main page that will bring the customer to this 'request-order-flow'. This is the main flow which needs to be full focus on the front page. All other items are secondary.
2. The general information of who we are and what we do, and why the customer should choose us. Preferably in short bullet-point type keywords/sentences with icons or other visual cues. See our unique selling points to get an idea of the information that will be displayed here.
3. There needs to be a section that will explain the process (see above) of a repair request step-by- step, again in brief short key sentences and with (custom) icons.
4. There needs to be a section that explains to the customer he/she can always contact us if they are not sure what the problem is with their device, and for this reason are not sure what repair request they should order.
5. We want to implement some functionality that display customer ratings or customer reviews. So there needs to be room for some kind of widget of plugin we're going to implement which shows these reviews.
6. A 'For business section' where we will explain all the options we provide for corporate clients.
7. Social media links.
8. There needs to be a menu with buttons that leads to the all sections described in the previous points.

For now, we need a design for our front page. In the second phase, when we have picked our winner, we may ask the winner to design the page(s) for our request workflow as well.

EDIT:
Finally, we have a very specific order in mind for the different segments of our website. We would like you to add some more segments that were not in our original brief as well:

1. Top header with order/request button. (should instantly make clear our main USP, we do repairs on location)
2. Our process
3. Our unique selling points / why choose us
4. The kind of repairs we do (broken screens, broken batteries, water damage, broken camera's, no sound etc.)
5. A 'meet our team' section, where we introduce some of our engineers
6. A 'contact us for any questions' section/
7. Testimonials/user reviews
8. A section where we show key performance indicators
9. 'For businesses' sections
10.'Subscribe for newsletter' field
11. Social media buttons

Industry/Entity Type

It Service

Number of Pages Required

1 page

Font styles to use
Sans Serif

Requirements
Must have
• a main/front page, design only
• custom icons/images for banners, adverts online and in print (high res)
Nice to have
• Storytelling in our design.
• Design that fits with our brand new logo.
• Elements like icons to have a flat design.
• Keep in mind that the website will need to be responsive when designing! (Ideally provide an example of the mobile design as well)
• Create a fun and trustworthy feeling.

```html
<!DOCTYPE html>
<html lang="en">
<head>
<meta charset="utf-8">
<title>Gadget Haven — Mobile repair on location</title>
<link href="https://fonts.googleapis.com/css2?family=Poppins:wght@300;400;500;600&family=Roboto:wght@400;500&display=swap" rel="stylesheet">
<style>
:root{
  --orange:#ee5a24;
  --orange-soft:#f26b38;
  --ink:#2b2d35;
  --text:#555a64;
  --muted:#9a9ea7;
  --line:#e4e6ea;
  --paper:#ffffff;
  --mist:#f1f2f4;
  --teal:#0b7d95;
  --teal-btn:#2a93a8;
  --night:#1d2230;
  --night-line:#343a4a;
  --tick:#5bbf8f;
}
*{box-sizing:border-box;margin:0;padding:0}
html,body{width:1200px;height:2736px;overflow:hidden}
body{font-family:"Roboto",Arial,sans-serif;color:var(--text);background:var(--paper);position:relative}
section,header,footer{position:relative;width:1200px}
.abs{position:absolute}
h1,h2,h3{font-family:"Poppins",Arial,sans-serif;font-weight:300;color:var(--ink)}
.accent-line{position:absolute;width:40px;height:2px;background:var(--orange)}

/* header */
.site-header{height:75px;background:var(--paper);border-bottom:1px solid var(--line)}
.brand{left:91px;top:14px;display:flex;align-items:center;gap:10px}
.brand-dot{width:40px;height:40px;border-radius:50%;background:var(--orange)}
.brand-name{font-family:"Poppins",sans-serif;font-weight:600;font-size:15px;line-height:17px;color:var(--ink);width:80px;text-transform:uppercase}
.main-nav{left:482px;top:0;height:75px;display:flex;align-items:center}
.main-nav a{font-family:"Poppins",sans-serif;font-size:13px;color:var(--ink);text-decoration:none;margin-right:37px}
.btn-request{left:983px;top:18px;width:128px;height:40px;border-radius:20px;background:var(--orange);color:#fff;font-family:"Poppins",sans-serif;font-size:13px;font-weight:500;display:flex;align-items:center;justify-content:center;text-decoration:none}

/* hero */
.hero{height:409px;background:linear-gradient(#fff,#fbfbfc)}
.hero h1{left:88px;top:150px;font-size:33px;white-space:nowrap;z-index:2}
.hero .lead{left:90px;top:196px;font-family:"Poppins",sans-serif;font-weight:300;font-size:18px;color:var(--ink);z-index:2}
.arrow-link{display:flex;align-items:center;gap:12px;font-family:"Poppins",sans-serif;font-size:12px;color:var(--orange);text-decoration:none}
.arrow-link .ring{width:26px;height:26px;border:1.5px solid var(--orange);border-radius:50%;display:flex;align-items:center;justify-content:center}
.hero .arrow-link{left:88px;top:238px}
.hero-scene{left:760px;top:50px;width:440px;height:359px;background:linear-gradient(90deg,#f3f4f6 0%,#f3f4f6 8%,#f06a3a 12%,#ee5a24 60%,#eef0f3 66%,#f5f6f8 100%)}
.hero-van{left:392px;top:290px;width:305px;height:118px;border-radius:22px 40px 8px 8px;background:linear-gradient(90deg,#eceef1,#dfe2e8)}

/* about */
.about{height:467px;background:var(--mist);overflow:hidden}
.phone-art{left:146px;top:73px;width:238px;height:420px;border-radius:26px;border:10px solid #fff;background:linear-gradient(160deg,#fdf1e9 0%,#fbe0d2 35%,#e2f3f0 70%,#f7f8fa 100%);box-shadow:0 2px 10px rgba(0,0,0,.05)}
.about .accent-line{left:503px;top:90px}
.about h2{left:503px;top:100px;font-size:28px}
.usp-list{left:503px;top:156px;list-style:none}
.usp-list li{display:flex;align-items:center;gap:11px;height:36px;font-size:12.5px;color:var(--text)}
.tick{width:14px;height:14px;border-radius:50%;background:var(--tick);display:flex;align-items:center;justify-content:center;flex:none}

/* process */
.process{height:380px;background:linear-gradient(var(--orange) 0,var(--orange) 202px,var(--paper) 202px)}
.process h2{left:0;width:1200px;text-align:center;top:58px;color:#fff;font-size:27px;font-weight:400}
.process .accent-line{background:#fff;left:580px;top:48px}
.process-card{left:89px;top:122px;width:1022px;height:258px;background:#fff;box-shadow:0 4px 18px rgba(0,0,0,.08)}
.steps{position:absolute;left:0;top:50px;width:100%;display:flex;justify-content:space-around;padding:0 18px}
.steps::before{content:"";position:absolute;left:120px;right:120px;top:44px;height:1px;background:var(--line)}
.step{width:170px;text-align:center;position:relative}
.step-icon{width:88px;height:88px;margin:0 auto;border-radius:50%;background:#fff;border:1px solid var(--line);display:flex;align-items:center;justify-content:center}
.step p{margin-top:22px;font-family:"Poppins",sans-serif;font-size:15px;line-height:24px;color:var(--text);font-weight:300}

/* reviews */
.reviews{height:462px;background:linear-gradient(#fff,#f3f4f6)}
.reviews .accent-line{left:580px;top:65px}
.reviews h2{left:0;width:1200px;text-align:center;top:74px;font-size:28px;font-weight:400}
.review{top:141px;width:320px;height:230px;background:#fff;border:1px solid #eceef1;padding:38px 30px}
.review.featured{box-shadow:0 10px 30px rgba(0,0,0,.1);border-color:transparent}
.review p{font-size:12.5px;line-height:22.5px;color:var(--text)}
.reviewer{position:absolute;left:30px;bottom:28px;display:flex;align-items:center;gap:14px}
.avatar{width:52px;height:52px;border-radius:50%;background:linear-gradient(#c9ccd2,#8d929c)}
.reviewer strong{display:block;font-family:"Poppins",sans-serif;font-weight:500;font-size:13px;color:var(--ink)}
.reviewer span{font-size:11px;color:var(--muted)}
.quote-mark{position:absolute;right:22px;bottom:0;font-family:"Poppins",sans-serif;font-size:72px;color:#e6e8eb;line-height:1}
.dots{left:0;width:1200px;top:414px;display:flex;justify-content:center;gap:8px}
.dots i{width:6px;height:6px;border-radius:50%;background:#c9ccd2}
.dots i.on{background:var(--ink)}

/* contact band */
.contact-band{height:220px;background:var(--teal)}
.contact-band .accent-line{background:#fff;left:88px;top:60px}
.contact-band h2{left:88px;top:70px;color:#fff;font-size:28px;font-weight:400}
.contact-band p{left:88px;top:115px;width:560px;color:#e2f1f4;font-size:12.5px;line-height:23px}
.btn-ghost{left:983px;top:88px;width:128px;height:44px;border-radius:22px;background:var(--teal-btn);color:#fff;font-family:"Poppins",sans-serif;font-size:13px;display:flex;align-items:center;justify-content:center;text-decoration:none}

/* business */
.business{height:395px;background:#fff}
.business .accent-line{left:88px;top:76px}
.business h2{left:88px;top:86px;font-size:28px;font-weight:400}
.business .copy{left:88px;top:136px;width:470px}
.business .copy p{font-size:12.5px;line-height:22.5px;margin-bottom:10px}
.business .arrow-link{left:88px;top:296px}
.business-art{left:720px;top:70px;width:395px;height:250px;background:linear-gradient(90deg,#f4f5f7 0%,#eef0f3 50%,#f7c5a8 100%);border-radius:4px}

/* footer */
.site-footer{height:328px;background:var(--night);color:#b8bcc6}
.newsletter-title{left:88px;top:20px;font-family:"Poppins",sans-serif;font-size:16px;color:#fff}
.newsletter-field{left:424px;top:18px;width:278px;height:30px;border-bottom:1px solid #8c92a0;display:flex;align-items:center;justify-content:space-between;font-size:11px;color:#a9aeb9}
.follow{left:923px;top:22px;display:flex;align-items:center;gap:14px;font-family:"Poppins",sans-serif;font-size:14px;color:#fff}
.social{width:12px;height:12px;border-radius:50%;background:#fff}
.footer-col{top:118px}
.footer-col h3{font-family:"Poppins",sans-serif;font-weight:500;font-size:16px;color:#fff;margin-bottom:18px}
.footer-col p{font-size:11.5px;line-height:22px;color:#b8bcc6}
.footer-col ul{list-style:none}
.footer-col li{font-size:11.5px;line-height:22px}
.footer-col li::before{content:"› "}
.footer-col .blog-title{font-family:"Poppins",sans-serif;font-weight:600;font-size:12px;color:#fff;margin-bottom:4px}
.footer-col em{color:var(--orange)}
.footer-rule{left:0;top:278px;width:1200px;height:1px;background:var(--night-line)}
.copyright{left:88px;top:295px;font-size:11px;color:#9aa0ab}
.to-top{left:1135px;top:265px;width:40px;height:40px;border-radius:50%;background:#fff;display:flex;align-items:center;justify-content:center}
</style>
</head>
<body>

<header class="site-header">
  <div class="brand abs"><span class="brand-dot"></span><span class="brand-name">Gadget Haven</span></div>
  <nav class="main-nav abs">
    <a href="#about">About</a><a href="#process">Process</a><a href="#contact">Contact</a><a href="#reviews">Customer Reviews</a><a href="#business">For Business</a>
  </nav>
  <a class="btn-request abs" href="#request">Request Order</a>
</header>

<section class="hero">
  <div class="hero-scene abs" role="img" aria-label="Illustration of an orange house with a technician waving at the door, grey city buildings behind"></div>
  <div class="hero-van abs" role="img" aria-label="Illustration of a white branded repair van parked by the road"></div>
  <h1 class="abs">We provide different services</h1>
  <p class="lead abs">for all kinds of electronic devices</p>
  <a class="arrow-link abs" href="#contact"><span class="ring"><svg width="12" height="10" viewBox="0 0 12 10"><path d="M0 5h10M6 1l4 4-4 4" stroke="#ee5a24" stroke-width="1.5" fill="none"/></svg></span>Contact us now</a>
</section>

<section class="about" id="about">
  <div class="phone-art abs" role="img" aria-label="Illustration of a white smartphone with a cracked screen showing colourful app icons"></div>
  <span class="accent-line"></span>
  <h2 class="abs">About the company</h2>
  <ul class="usp-list abs">
    <li><span class="tick"><svg width="8" height="6" viewBox="0 0 8 6"><path d="M1 3l2 2 4-4" stroke="#fff" stroke-width="1.5" fill="none"/></svg></span>Professional service on location. Don't ship to us we will come to you!</li>
    <li><span class="tick"><svg width="8" height="6" viewBox="0 0 8 6"><path d="M1 3l2 2 4-4" stroke="#fff" stroke-width="1.5" fill="none"/></svg></span>Clear pricing upfront. No hidden cost.</li>
    <li><span class="tick"><svg width="8" height="6" viewBox="0 0 8 6"><path d="M1 3l2 2 4-4" stroke="#fff" stroke-width="1.5" fill="none"/></svg></span>Next business-day repair.</li>
    <li><span class="tick"><svg width="8" height="6" viewBox="0 0 8 6"><path d="M1 3l2 2 4-4" stroke="#fff" stroke-width="1.5" fill="none"/></svg></span>Backed by a professional call center open 12 hours a day and open on a Saturday as well</li>
    <li><span class="tick"><svg width="8" height="6" viewBox="0 0 8 6"><path d="M1 3l2 2 4-4" stroke="#fff" stroke-width="1.5" fill="none"/></svg></span>Backed by a professional repair center with more then 12 years of experience</li>
    <li><span class="tick"><svg width="8" height="6" viewBox="0 0 8 6"><path d="M1 3l2 2 4-4" stroke="#fff" stroke-width="1.5" fill="none"/></svg></span>Repair is done by certified engineers</li>
    <li><span class="tick"><svg width="8" height="6" viewBox="0 0 8 6"><path d="M1 3l2 2 4-4" stroke="#fff" stroke-width="1.5" fill="none"/></svg></span>1 year warranty on the repair</li>
  </ul>
</section>

<section class="process" id="process">
  <span class="accent-line"></span>
  <h2 class="abs">The Process</h2>
  <div class="process-card abs">
    <div class="steps">
      <div class="step">
        <div class="step-icon"><svg width="44" height="44" viewBox="0 0 44 44"><rect x="10" y="6" width="20" height="34" rx="3" fill="#3b4150"/><rect x="12" y="10" width="16" height="24" fill="#e9ecf1"/><rect x="22" y="8" width="16" height="11" rx="2" fill="#ee5a24"/><path d="M26 19l-2 4 5-4z" fill="#ee5a24"/></svg></div>
        <p>Choose your device<br>and repair job</p>
      </div>
      <div class="step">
        <div class="step-icon"><svg width="44" height="44" viewBox="0 0 44 44"><rect x="9" y="6" width="24" height="32" rx="2" fill="#5fc9b4"/><path d="M13 14l2 2 3-3M13 22l2 2 3-3M13 30l2 2 3-3" stroke="#fff" stroke-width="1.5" fill="none"/><path d="M21 15h8M21 23h8M21 31h6" stroke="#fff" stroke-width="1.5"/><circle cx="33" cy="33" r="6" fill="#ee5a24"/><path d="M30 33l2 2 4-4" stroke="#fff" stroke-width="1.5" fill="none"/></svg></div>
        <p>Place the<br>Order</p>
      </div>
      <div class="step">
        <div class="step-icon"><svg width="44" height="44" viewBox="0 0 44 44"><rect x="11" y="6" width="20" height="34" rx="3" fill="#3b4150"/><rect x="13" y="10" width="16" height="24" fill="#f3e6d9"/><circle cx="29" cy="28" r="7" fill="#ee5a24"/><path d="M29 24v4h3" stroke="#fff" stroke-width="1.5" fill="none"/></svg></div>
        <p>Get a callback<br>within an hour</p>
      </div>
      <div class="step">
        <div class="step-icon"><svg width="44" height="44" viewBox="0 0 44 44"><rect x="7" y="10" width="30" height="26" rx="2" fill="#e9ecf1"/><rect x="7" y="10" width="30" height="7" fill="#3b4150"/><path d="M13 22h3M19 22h3M25 22h3M13 28h3M19 28h3" stroke="#9aa0ab" stroke-width="2"/><circle cx="30" cy="30" r="6" fill="#ee5a24"/><path d="M30 27a2 2 0 0 1 2 2c0 2-2 4-2 4s-2-2-2-4a2 2 0 0 1 2-2z" fill="#fff"/></svg></div>
        <p>Set date &amp;<br>location</p>
      </div>
      <div class="step">
        <div class="step-icon"><svg width="44" height="44" viewBox="0 0 44 44"><path d="M8 22L22 10l14 12" stroke="#ee5a24" stroke-width="3" fill="none"/><rect x="12" y="21" width="20" height="15" fill="#7aa6d8"/><rect x="19" y="27" width="6" height="9" fill="#3b4150"/><rect x="14" y="24" width="4" height="4" fill="#fff"/><rect x="26" y="24" width="4" height="4" fill="#fff"/></svg></div>
        <p>We will come<br>to you</p>
      </div>
    </div>
  </div>
</section>

<section class="reviews" id="reviews">
  <span class="accent-line"></span>
  <h2 class="abs">Customer Reviews</h2>
  <article class="review abs" style="left:89px">
    <p>Aenean vulputate eleifend tellus aenean leo ligula porttitor eu, consequat vitae eleifend ac enim aliquam lorem ante dapibus in viverra quis feugiat a tellus.</p>
    <div class="reviewer"><div class="avatar" role="img" aria-label="Portrait photo of the reviewer"></div><div><strong>Lena Vos</strong><span>@lena</span></div></div>
    <span class="quote-mark">&ldquo;</span>
  </article>
  <article class="review featured abs" style="left:440px">
    <p>Aenean vulputate eleifend tellus aenean leo ligula porttitor eu, consequat vitae eleifend ac enim aliquam lorem ante dapibus in viverra quis feugiat a tellus.</p>
    <div class="reviewer"><div class="avatar" role="img" aria-label="Portrait photo of the reviewer"></div><div><strong>Bram Kool</strong><span>@bram</span></div></div>
    <span class="quote-mark">&ldquo;</span>
  </article>
  <article class="review abs" style="left:791px">
    <p>Aenean vulputate eleifend tellus aenean leo ligula porttitor eu, consequat vitae eleifend ac enim aliquam lorem ante dapibus in viverra quis feugiat a tellus.</p>
    <div class="reviewer"><div class="avatar" role="img" aria-label="Portrait photo of the reviewer"></div><div><strong>Milo Brandt</strong><span>@milo</span></div></div>
    <span class="quote-mark">&ldquo;</span>
  </article>
  <div class="dots abs"><i class="on"></i><i></i><i></i></div>
</section>

<section class="contact-band" id="contact">
  <span class="accent-line"></span>
  <h2 class="abs">If not sure about the problem, Contact Us</h2>
  <p class="abs">You can always contact us if you are not sure what the problem is with your device, and you are not sure what repair request you should order.</p>
  <a class="btn-ghost abs" href="#contact">Contact us</a>
</section>

<section class="business" id="business">
  <span class="accent-line"></span>
  <h2 class="abs">For Business</h2>
  <div class="copy abs">
    <p>In enim justo rhoncus ut imperdiet a venenatis vitae, justo nullam dictum felis eu pede mollis pretium integer tincidunt cras dapibus. Vivamus elementum semper nisi aenean vulputate.</p>
    <p>Maecenas nec odio et ante tincidunt tempus donec vitae sapien ut libero venenatis faucibus nullam quis ante etiam sit amet orci eget eros faucibus tincidunt duis leo sed fringilla mauris sit.</p>
  </div>
  <a class="arrow-link abs" href="#business"><span class="ring"><svg width="12" height="10" viewBox="0 0 12 10"><path d="M0 5h10M6 1l4 4-4 4" stroke="#ee5a24" stroke-width="1.5" fill="none"/></svg></span>Learn More</a>
  <div class="business-art abs" role="img" aria-label="Illustration of a person working at a laptop on a desk in an office with shelves"></div>
</section>

<footer class="site-footer">
  <p class="newsletter-title abs">Subscribe to our email newsletter</p>
  <div class="newsletter-field abs"><span>Enter email address...</span><svg width="14" height="14" viewBox="0 0 14 14"><path d="M1 7l12-6-4 12-2-5z" fill="#ee5a24"/></svg></div>
  <div class="follow abs">Follow us:
    <span class="social" role="img" aria-label="Social network link"></span>
    <span class="social" role="img" aria-label="Social network link"></span>
    <span class="social" role="img" aria-label="Social network link"></span>
    <span class="social" role="img" aria-label="Social network link"></span>
  </div>
  <div class="footer-col abs" style="left:88px;width:420px">
    <h3>About</h3>
    <p>Nullam dictum felis eu pede mollis pretium integer tincidunt cras dapibus vivamus elementum semper nisi aenean vulputate eleifend tellus aenean leo ligula porttitor eu consequat vitae eleifend ac.</p>
  </div>
  <div class="footer-col abs" style="left:578px">
    <h3>Useful Links</h3>
    <ul><li>Home</li><li>Privacy Policy</li><li>Terms &amp; Conditions</li></ul>
  </div>
  <div class="footer-col abs" style="left:792px;width:320px">
    <h3>Blogs</h3>
    <p class="blog-title">BLOG 1</p>
    <p>Nullam dictum felis eu pede mollis pretium integer tincid-unt cras dapibus. <em>Read Blog</em></p>
  </div>
  <div class="footer-rule abs"></div>
  <p class="copyright abs">© 2017, All Rights Reserved.</p>
  <a class="to-top abs" href="#top" aria-label="Back to top"><svg width="12" height="12" viewBox="0 0 12 12"><path d="M6 11V2M2 5l4-4 4 4" stroke="#2b2d35" stroke-width="1.5" fill="none"/></svg></a>
</footer>

</body>
</html>
```